Business card design needed

I need a business card for my private practice. I would like to see the designs that use bright blue and white. I would like to see similar designs as to the card below:
http://blog.printvarno.com/2009/designing-a-business-card-with-pv-ks517-template.html
I would like to see the back of the card have room for appointment times. Thank you.

Industry/Entity Type
Business
Contact Information for Business Card
Brightwater Counselling & Wellness Services
Helen Dorsey B.Psychology
Registered Psychologist
Building C, Level 3, 14 Marrow Crescent, Canberra, ACT 2601
T: (02) 6287 5912
F: (02) 6287 5930
info@brightwatercounselling.com.au
www.brightwatercounselling.com.au

```html
<!DOCTYPE html>
<html lang="en">
<head>
<meta charset="utf-8">
<title>Brightwater Counselling &amp; Wellness Services – Business Card</title>
<link href="https://fonts.googleapis.com/css2?family=Tinos:wght@400;700&display=swap" rel="stylesheet">
<style>
  :root {
    --backdrop: #262626;
    --navy: #26246b;
    --navy-deep: #111040;
    --navy-glow: #2e2f8a;
    --ink: #1a1a1a;
    --paper: #ffffff;
    --serif: "Tinos", "Times New Roman", serif;
  }
  * { margin: 0; padding: 0; box-sizing: border-box; }
  html, body { width: 1200px; height: 1200px; overflow: hidden; }
  body {
    background: var(--backdrop);
    font-family: var(--serif);
    display: flex;
    flex-direction: column;
    align-items: center;
    justify-content: center;
    gap: 40px;
  }
  .card {
    width: 945px;
    height: 540px;
    position: relative;
    overflow: hidden;
  }

  /* Front */
  .card-front {
    background: radial-gradient(ellipse at 50% 45%, var(--navy-glow) 0%, var(--navy) 40%, var(--navy-deep) 100%);
    display: flex;
    align-items: center;
    justify-content: center;
  }
  .brand {
    display: flex;
    align-items: center;
    gap: 22px;
  }
  .brand-mark {
    width: 34px;
    height: 34px;
    flex: none;
  }
  .brand-name {
    font-weight: 700;
    font-size: 34px;
    line-height: 1.15;
    max-width: 380px;
  }
  .card-front .brand-mark { background: var(--paper); }
  .card-front .brand-name { color: var(--paper); }

  /* Back */
  .card-back { background: var(--paper); }
  .accent-bar {
    position: absolute;
    width: 30px;
    background: var(--navy);
  }
  .accent-bar.left { left: 0; top: 220px; height: 260px; }
  .accent-bar.right { right: 0; top: 40px; height: 200px; }

  .card-back .brand {
    position: absolute;
    left: 75px;
    top: 150px;
  }
  .card-back .brand-mark { background: var(--navy); }
  .card-back .brand-name { color: var(--navy); font-size: 30px; max-width: 300px; }

  .divider {
    position: absolute;
    left: 440px;
    top: 70px;
    width: 6px;
    height: 320px;
    background: var(--navy);
  }

  .contact {
    position: absolute;
    left: 475px;
    top: 60px;
    color: var(--ink);
    font-size: 21px;
    line-height: 1.12;
  }
  .contact-name {
    font-size: 38px;
    line-height: 1.05;
    font-weight: 400;
  }
  .contact-name .given { color: var(--navy); }
  .credentials { color: var(--navy); }
  .address { margin: 10px 0 0 80px; }
  .phones { margin: 24px 0 0 30px; }
  .phones dt { display: inline-block; width: 34px; color: var(--navy); }
  .phones dd { display: inline; }
  .web { margin-top: 24px; color: var(--navy); }

  .appointment {
    position: absolute;
    left: 75px;
    right: 60px;
    bottom: 40px;
    font-size: 28px;
  }
  .appointment-title { color: var(--navy); font-size: 32px; margin-bottom: 10px; }
  .slots { display: flex; gap: 20px; color: var(--ink); }
  .slot { flex: 1; display: flex; align-items: baseline; gap: 8px; }
  .slot::after {
    content: "";
    flex: 1;
    border-bottom: 2px dotted var(--ink);
  }
</style>
</head>
<body>

  <section class="card card-front" aria-label="Card front">
    <div class="brand">
      <span class="brand-mark"></span>
      <span class="brand-name">Brightwater Counselling &amp; Wellness Services</span>
    </div>
  </section>

  <section class="card card-back" aria-label="Card back">
    <span class="accent-bar left"></span>
    <span class="accent-bar right"></span>

    <div class="brand">
      <span class="brand-mark"></span>
      <span class="brand-name">Brightwater Counselling &amp; Wellness Services</span>
    </div>

    <span class="divider"></span>

    <div class="contact">
      <h1 class="contact-name"><span class="given">Helen</span> Dorsey</h1>
      <p class="credentials">B.Psychology</p>
      <p class="role">Psychologist</p>
      <address class="address" style="font-style:normal">
        Building C, Level 3<br>
        14 Marrow Crescent<br>
        Canberra, ACT 2601
      </address>
      <dl class="phones">
        <div><dt>T</dt><dd>(02) 6287 5912</dd></div>
        <div><dt>F</dt><dd>(02) 6287 5930</dd></div>
      </dl>
      <p class="web">info@brightwatercounselling.com.au<br>www.brightwatercounselling.com.au</p>
    </div>

    <div class="appointment">
      <p class="appointment-title">Next appointment</p>
      <div class="slots">
        <span class="slot">Day</span>
        <span class="slot">Date</span>
        <span class="slot">Time</span>
      </div>
    </div>
  </section>

</body>
</html>
```